Silver Dart Shiners packaging design

We need a packaging design for Kestner Trailworks LLC. The Brand Name is Silver Dart Shiners, this is a fishing lure that was developed by a Inland Angling Honor Roll Society inductee. We would like to see the designs that use the color green in the packaging. the final design should represent quality. excitement and Innovation. The Package size is 3 inches wide and 4 inches tall, this will be a pegged package so the front of the package is all that will need to be designed.
Target Market(s)
age 25-55 Male and Female
Logo Text
Tough and represents quality
Requirements
Must have
- Silver Dart Shiners as logo
- Tagline Inspired a World Record Fishing Title
- Notes not what to say but have it represented in the design: Bold and strength contemporary and sharp
Nice to have
- na
Should not have
- na

```html
<!DOCTYPE html>
<html lang="en">
<head>
<meta charset="utf-8">
<title>Silver Dart Shiners – Pegged Package Front</title>
<link rel="stylesheet" href="https://fonts.googleapis.com/css2?family=Anton&family=Open+Sans:wght@600;700;800&display=swap">
<style>
  :root {
    --page-bg: #ececee;
    --card-rim: #f4f6f2;
    --water-deep: #1f6b34;
    --water-mid: #3f9a4f;
    --water-light: #8cc98a;
    --ink: #0d0d0d;
    --accent: #e8452a;
    --ribbon: #f0531f;
    --ribbon-text: #fff6e8;
    --white: #ffffff;
    --lure-body: #e9a54a;
    --lure-light: #f7e0b2;
    --swatch-yellow: #f2e21c;
    --swatch-pink: #ee3d95;
    --swatch-orange: #f28a1e;
  }
  html, body {
    margin: 0;
    width: 1200px;
    height: 1200px;
    overflow: hidden;
    background: var(--page-bg);
  }
  .canvas {
    position: relative;
    width: 1200px;
    height: 1200px;
  }
  .package-card {
    position: absolute;
    left: 210px;
    top: 80px;
    width: 780px;
    height: 1040px;
    border-radius: 30px;
    border: 5px solid var(--card-rim);
    box-sizing: border-box;
    overflow: hidden;
    box-shadow: 0 18px 40px rgba(0,0,0,0.18);
  }
  .underwater-scene {
    position: absolute;
    inset: 0;
    background:
      radial-gradient(ellipse 70% 30% at 55% 55%, rgba(200,240,190,0.55), transparent 70%),
      linear-gradient(180deg, var(--water-mid) 0%, var(--water-light) 45%, var(--water-mid) 60%, var(--water-deep) 100%);
  }
  .peg-hole {
    position: absolute;
    left: 250px;
    top: 78px;
    width: 287px;
    height: 59px;
    border-radius: 20px;
    background: var(--white);
  }
  .quality-ribbon {
    position: absolute;
    left: 0;
    top: 0;
    width: 770px;
    height: 300px;
  }
  .quality-ribbon text {
    font-family: "Open Sans", sans-serif;
    font-weight: 800;
    font-size: 29px;
    fill: var(--ribbon-text);
    letter-spacing: 1px;
  }
  .brand-logo {
    position: absolute;
    left: 0;
    right: 0;
    top: 0;
    margin: 0;
    font-family: "Anton", sans-serif;
    font-weight: 400;
    color: var(--ink);
    text-transform: uppercase;
  }
  .brand-logo span {
    position: absolute;
    left: 0;
    right: 0;
    text-align: center;
    line-height: 1;
    white-space: nowrap;
  }
  .brand-logo .line-one {
    top: 160px;
    font-size: 86px;
    letter-spacing: 3px;
  }
  .brand-logo .line-two {
    top: 252px;
    font-size: 86px;
    letter-spacing: 3px;
  }
  .tagline {
    position: absolute;
    left: 0;
    right: 0;
    top: 366px;
    margin: 0;
    text-align: center;
    font-family: "Open Sans", sans-serif;
    font-weight: 800;
    font-size: 30px;
    color: var(--accent);
  }
  .blister {
    position: absolute;
    left: 120px;
    top: 430px;
    width: 620px;
    height: 490px;
    border-radius: 26px;
    background: rgba(255,255,255,0.12);
    border: 2px solid rgba(255,255,255,0.35);
    box-sizing: border-box;
    box-shadow: inset 0 0 30px rgba(255,255,255,0.18);
  }
  .lure-photo {
    position: absolute;
    left: 55px;
    top: 45px;
    width: 500px;
    height: 380px;
    border-radius: 24px;
    background: linear-gradient(135deg, var(--lure-light) 0%, var(--lure-body) 100%);
  }
  .color-options {
    position: absolute;
    left: 55px;
    top: 928px;
    font-family: "Open Sans", sans-serif;
  }
  .color-options .label {
    display: block;
    font-weight: 700;
    font-size: 17px;
    color: var(--white);
    margin: 0 0 4px 22px;
  }
  .swatch-pill {
    display: flex;
    gap: 14px;
    align-items: center;
    width: 203px;
    height: 52px;
    box-sizing: border-box;
    padding: 0 22px;
    border: 3px solid var(--white);
    border-radius: 26px;
  }
  .swatch {
    width: 36px;
    height: 20px;
    border-radius: 50%;
  }
  .swatch.yellow { background: var(--swatch-yellow); }
  .swatch.pink { background: var(--swatch-pink); }
  .swatch.orange { background: var(--swatch-orange); }
  .contact-block {
    position: absolute;
    right: 52px;
    top: 930px;
    text-align: right;
    font-family: "Open Sans", sans-serif;
    color: var(--white);
    font-weight: 700;
  }
  .contact-block p { margin: 0; font-size: 19px; line-height: 1.2; }
  .contact-block .web { font-size: 23px; font-weight: 800; margin-top: 10px; }
</style>
</head>
<body>
<main class="canvas">
  <section class="package-card">
    <div class="underwater-scene" role="img" aria-label="Underwater scene in green tones with light rays and rising bubbles"></div>
    <div class="peg-hole"></div>

    <svg class="quality-ribbon" viewBox="0 0 770 300" aria-label="High quality ribbon">
      <polygon points="495,0 615,0 770,125 770,222" fill="var(--ribbon)"/>
      <text transform="translate(660,86) rotate(38.9)" text-anchor="middle" dominant-baseline="central">HIGH QUALITY</text>
    </svg>

    <h1 class="brand-logo">
      <span class="line-one">Silver Dart</span>
      <span class="line-two">Shiners</span>
    </h1>
    <p class="tagline">Inspired a World Record Fishing Title</p>

    <div class="blister">
      <div class="lure-photo" role="img" aria-label="Photo of an orange soft minnow lure with red treble hook and swivel"></div>
    </div>

    <div class="color-options">
      <span class="label">Color</span>
      <div class="swatch-pill">
        <span class="swatch yellow"></span>
        <span class="swatch pink"></span>
        <span class="swatch orange"></span>
      </div>
    </div>

    <div class="contact-block">
      <p>More information</p>
      <p>please contact: 01 5550 4821</p>
      <p class="web">www.kestnertrailworks.com</p>
    </div>
  </section>
</main>
</body>
</html>
```